Brochure design for healthcare software company

We need a tri-fold brochure design for our healthcare software company that provides software and services for clinicians who manage patients who have or may be diagnosed with cancer.

We have an existing web, business card design and trade show booth design and want the ultimate design to be consistent with these. All of the files including stock images are provided.

Target Market(s)

Nurses, Healthcare professionals

Industry/Entity Type

Healthcare

Requirements
Must have
• Design consistent with attached tradeshow booth and business card.

```html
<!DOCTYPE html>
<html lang="en">
<head>
<meta charset="utf-8">
<title>Clarivance Patient Navigation – Tri-fold Brochure</title>
<link rel="stylesheet" href="https://fonts.googleapis.com/css2?family=Lato:wght@400;700&family=Tenor+Sans&display=swap">
<style>
  :root {
    --green: #12c47f;
    --green-light: #22dd92;
    --green-dark: #0ea86b;
    --blue: #1256b8;
    --blue-dark: #0b3f93;
    --blue-light: #5a92dd;
    --ink: #2b2b2b;
    --grey: #d9dadd;
    --paper: #ffffff;
    --stage: #e9eaec;
  }
  * { box-sizing: border-box; margin: 0; padding: 0; }
  html, body { width: 1200px; height: 810px; overflow: hidden; background: var(--stage); }
  body { font-family: "Lato", Arial, sans-serif; position: relative; }

  .spread {
    position: absolute; left: 90px; top: 10px;
    width: 1020px; height: 790px;
    display: flex; background: var(--paper);
    box-shadow: 0 6px 24px rgba(0,0,0,.18);
    overflow: hidden;
  }
  .panel { position: relative; width: 340px; height: 790px; overflow: hidden; }

  /* Features panel */
  .panel--features { background: linear-gradient(160deg, var(--green-dark), var(--green-light) 70%); padding: 34px 30px 0; color: #fff; }
  .feature { margin-bottom: 16px; }
  .feature__title {
    display: inline-block; background: #fff; color: var(--blue);
    font-size: 13.5px; font-weight: 700; padding: 3px 11px; margin-bottom: 7px;
  }
  .feature__text { font-size: 11.5px; line-height: 1.45; }

  /* Contact panel */
  .panel--contact { background: var(--paper); padding: 70px 36px 0; }
  .contact__title { color: var(--green); font-size: 20px; font-weight: 700; letter-spacing: .5px; margin-bottom: 12px; }
  .contact__row { display: flex; align-items: center; gap: 8px; color: var(--ink); margin-bottom: 6px; font-size: 11px; }
  .contact__row--phone { font-size: 21px; }
  .contact__row--web { letter-spacing: 1.5px; }
  .contact__row svg { flex: none; }
  .brand-mark { display: flex; flex-direction: column; align-items: center; gap: 10px; }
  .brand-mark__square { width: 46px; height: 46px; background: var(--green); }
  .brand-mark__name { font-family: "Lato", Arial, sans-serif; font-size: 11px; letter-spacing: 4px; color: var(--ink); }
  .panel--contact .brand-mark { margin-top: 64px; }

  .bottom-art { position: absolute; left: 0; top: 440px; width: 680px; height: 350px; }

  /* Cover panel */
  .panel--cover { background: var(--paper); }
  .cover__art { position: absolute; inset: 0; }
  .panel--cover .brand-mark { position: absolute; top: 44px; left: 0; right: 0; }
  .cover__text { position: absolute; left: 26px; right: 18px; top: 606px; }
  .cover__title { font-family: "Tenor Sans", "Lato", sans-serif; color: var(--blue); font-size: 29px; line-height: 1.15; font-weight: 400; white-space: nowrap; }
  .cover__subtitle { font-size: 11px; color: var(--ink); margin-top: 8px; line-height: 1.35; }
  .cover__footer {
    position: absolute; left: 0; right: 0; bottom: 0; height: 50px;
    background: var(--blue); color: #fff; display: flex; align-items: center; justify-content: center;
    font-size: 15px; letter-spacing: 2px; font-weight: 700;
  }
</style>
</head>
<body>
<main class="spread">

  <section class="panel panel--features">
    <article class="feature">
      <h3 class="feature__title">Simplified navigation</h3>
      <p class="feature__text">Track all of your patients from their entry point, for example an abnormal screening exam or a positive diagnosis, through survivorship. Clarivance Navigation allows you to easily maintain a record of all referrals, exams, treatments, contacts, appointments and notes for your patients.</p>
    </article>
    <article class="feature">
      <h3 class="feature__title">Advanced workflow tools</h3>
      <p class="feature__text">View and manage your entire patient load in a single dynamic work list area. Completely customizable to match your workflow. Create checklists for every step of your workflow to maintain consistent patient care and monitoring.</p>
    </article>
    <article class="feature">
      <h3 class="feature__title">Reporting and analytics</h3>
      <p class="feature__text">Quickly demonstrate the value of your navigation efforts with deep analytics and reporting. View current and historical trends for any or all of your facilities and staff, including detailed reporting on work loads, time to care, patient barriers, referrals and appointments.</p>
    </article>
    <article class="feature">
      <h3 class="feature__title">Eliminate paper</h3>
      <p class="feature__text">Manage all of your paperwork and patient forms in one easy to use area. Automatically create document packets and auto fill forms for patients or referrals with a single click.</p>
    </article>
  </section>

  <section class="panel panel--contact">
    <h2 class="contact__title">CONTACT US:</h2>
    <p class="contact__row">
      <svg width="12" height="9" viewBox="0 0 12 9"><rect x=".5" y=".5" width="11" height="8" fill="none" stroke="#555"/><path d="M.5 .5 6 5 11.5 .5" fill="none" stroke="#555"/></svg>
      sales@clarivance-health.com
    </p>
    <p class="contact__row">
      <svg width="12" height="9" viewBox="0 0 12 9"><rect x=".5" y=".5" width="11" height="8" fill="none" stroke="#555"/><path d="M.5 .5 6 5 11.5 .5" fill="none" stroke="#555"/></svg>
      support@clarivance-health.com
    </p>
    <p class="contact__row contact__row--phone">
      <svg width="16" height="16" viewBox="0 0 16 16"><circle cx="8" cy="8" r="7.2" fill="none" stroke="#333" stroke-width="1.4"/><path d="M5.3 4.2 6.6 4 7.3 6 6.4 6.8q.8 1.7 2.6 2.7l.8-.9 2 .8-.2 1.3q-.6.8-1.6.6Q6.5 10.2 4.7 5.8q0-1 .6-1.6z" fill="#333"/></svg>
      (855) 555-0147
    </p>
    <p class="contact__row contact__row--web">
      <svg width="12" height="12" viewBox="0 0 12 12"><circle cx="6" cy="6" r="5.3" fill="none" stroke="#555"/><ellipse cx="6" cy="6" rx="2.3" ry="5.3" fill="none" stroke="#555"/><path d="M.7 6h10.6" stroke="#555"/></svg>
      www.clarivance-health.com
    </p>
    <div class="brand-mark">
      <span class="brand-mark__square"></span>
      <span class="brand-mark__name">CLARIVANCE</span>
    </div>
  </section>

  <section class="panel panel--cover">
    <svg class="cover__art" width="340" height="790" viewBox="0 0 340 790">
      <defs>
        <linearGradient id="clinicTone" x1="0" y1="0" x2="1" y2="1">
          <stop offset="0" stop-color="#c9b8a6"/>
          <stop offset=".45" stop-color="#e7e4e0"/>
          <stop offset="1" stop-color="#6fa9c6"/>
        </linearGradient>
      </defs>
      <polygon points="0,0 100,0 0,90" fill="var(--green)"/>
      <polygon points="0,150 340,230 340,260 0,260" fill="var(--grey)"/>
      <g role="img" aria-label="Photo of a smiling nurse seated at a desk with a laptop in a bright clinic">
        <polygon points="0,200 340,250 340,560 0,500" fill="url(#clinicTone)"/>
      </g>
      <polygon points="0,500 340,560 340,578 0,518" fill="var(--blue-light)"/>
      <polygon points="0,512 340,572 340,596 0,536" fill="var(--blue)"/>
    </svg>
    <div class="brand-mark">
      <span class="brand-mark__square"></span>
      <span class="brand-mark__name">CLARIVANCE</span>
    </div>
    <div class="cover__text">
      <h1 class="cover__title">Clarivance<br>Patient Navigation</h1>
      <p class="cover__subtitle">Streamlining your oncology patient navigation workflow to reach optimal outcomes for your patients</p>
    </div>
    <div class="cover__footer">www.clarivance-health.com</div>
  </section>

  <svg class="bottom-art" width="680" height="350" viewBox="0 0 680 350">
    <defs>
      <linearGradient id="officeTone" x1="0" y1="0" x2="1" y2="1">
        <stop offset="0" stop-color="#4a3b2c"/>
        <stop offset=".5" stop-color="#c9a98a"/>
        <stop offset="1" stop-color="#8fa7d6"/>
      </linearGradient>
    </defs>
    <path d="M0,250 Q340,170 680,40 L680,350 L0,350 Z" fill="#fff"/>
    <path d="M0,264 Q340,184 680,54 L680,350 L0,350 Z" fill="var(--blue-dark)"/>
    <path d="M0,282 Q340,202 680,72 L680,350 L0,350 Z" fill="var(--blue-light)"/>
    <path d="M0,294 Q340,214 680,84 L680,350 L0,350 Z" fill="#fff"/>
    <g role="img" aria-label="Photo of a nurse talking on the phone at a desk beside patient file folders">
      <path d="M0,304 Q340,224 680,94 L680,350 L0,350 Z" fill="url(#officeTone)"/>
    </g>
  </svg>

</main>
</body>
</html>
```